Company director needs a business card design

I am a semi-retired former senior finance executive who sits on a number of public and private company boards and do some consulting work. I work largely with emerging businesses but deal regularly with top end of town lawyers, bankers etc. I need a thoughtful but relatively conservative design which would also resonate with my younger client base. Some colour would be good. Information limited to name, address, office tel, mobile and email.

Industry/Entity Type

Finance

```html
<!DOCTYPE html>
<html lang="en">
<head>
<meta charset="utf-8">
<title>Daniel Whitford – Business Card</title>
<link rel="stylesheet" href="https://fonts.googleapis.com/css2?family=Questrial&display=swap">
<style>
  :root {
    --backdrop: #e6e9ee;
    --card: #ffffff;
    --navy: #16294f;
    --name: #1b2e58;
    --title: #7d8b94;
    --band-text: #c6d0e0;
  }
  * { margin: 0; padding: 0; box-sizing: border-box; }
  html, body {
    width: 1200px;
    height: 720px;
    overflow: hidden;
    background: var(--backdrop);
    font-family: "Questrial", "Century Gothic", sans-serif;
  }
  .canvas {
    width: 1200px;
    height: 720px;
    display: flex;
    align-items: center;
    justify-content: center;
  }
  .card {
    width: 1000px;
    height: 600px;
    background: var(--card);
    display: flex;
    flex-direction: column;
    box-shadow: 0 6px 24px rgba(20, 35, 70, 0.18);
  }
  .card-identity {
    flex: 1;
    display: flex;
    flex-direction: column;
    align-items: center;
    padding-top: 110px;
  }
  .holder-name {
    color: var(--name);
    font-size: 76px;
    font-weight: 400;
    letter-spacing: 2px;
    line-height: 1;
  }
  .holder-title {
    color: var(--title);
    font-size: 36px;
    letter-spacing: 2px;
    margin-top: 14px;
    padding-left: 40px;
  }
  .contact-band {
    height: 170px;
    background: var(--navy);
    color: var(--band-text);
    font-size: 24px;
    letter-spacing: 1px;
    display: grid;
    grid-template-columns: 320px 1fr auto;
    padding: 36px 40px 0 40px;
    line-height: 1.75;
  }
  .contact-email { padding-left: 16px; }
  .contact-phones { text-align: right; }
</style>
</head>
<body>
<main class="canvas">
  <article class="card">
    <header class="card-identity">
      <h1 class="holder-name">Daniel Whitford</h1>
      <p class="holder-title">Finance Executive</p>
    </header>
    <footer class="contact-band">
      <address class="contact-address" style="font-style: normal;">
        18 Harbourview Street,<br>
        Seaview NSW 2090
      </address>
      <p class="contact-email">E: daniel_whitford@mailbox.net.au</p>
      <p class="contact-phones">
        T: 02 9000 1234<br>
        P: 0400 555 182
      </p>
    </footer>
  </article>
</main>
</body>
</html>
```